FR banner

we need a banner design (36"x120" horizontal) that will be displayed on a local high school baseball field. My company ( Crestwell Prints Co) has been producing signage for the Fernmoor Ridge community since 2009. We would like to communicate that we do more than banners. The final design should include the slogan "Signs Shirts Swag" and our Logo.

Target Market(s)

companies, teams, events, shirt and other marketing items.

Industry/Entity Type

Sign, Print,

Font styles to use
Sans Serif

Requirements
Should not have
• no baseball content.

```html
<!DOCTYPE html>
<html lang="en">
<head>
<meta charset="utf-8">
<title>Crestwell Prints Co — Signs Shirts Swag Banner</title>
<link rel="stylesheet" href="https://fonts.googleapis.com/css2?family=Montserrat:wght@400;700;800&display=swap">
<style>
  :root {
    --ink: #000000;
    --paper: #ffffff;
    --backdrop: #c9c9c9;
  }
  html, body {
    margin: 0;
    padding: 0;
    width: 909px;
    height: 1200px;
    overflow: hidden;
    background: var(--backdrop);
  }
  .canvas {
    position: relative;
    width: 909px;
    height: 1200px;
  }
  .banner {
    position: absolute;
    left: 29px;
    top: 472px;
    width: 850px;
    height: 256px;
    display: block;
  }
  .banner__paper { fill: var(--paper); }
  .banner__ink { fill: var(--ink); }
  .checkbox { fill: var(--paper); }
  .service {
    font-family: "Montserrat", sans-serif;
    font-weight: 400;
    font-size: 70px;
    letter-spacing: 0.1em;
    fill: var(--paper);
  }
  .tagline-strip { fill: var(--paper); }
  .tagline {
    font-family: "Montserrat", sans-serif;
    font-weight: 700;
    font-size: 15.5px;
    letter-spacing: 0.22em;
    fill: var(--ink);
  }
  .brand-name {
    font-family: "Montserrat", sans-serif;
    font-weight: 800;
    font-size: 27px;
    letter-spacing: 0.02em;
    fill: var(--ink);
  }
  .brand-mark { fill: var(--ink); }
</style>
</head>
<body>
<main class="canvas">
  <svg class="banner" viewBox="0 0 850 256" role="group" aria-label="Crestwell Prints Co banner: Signs, Shirts, Swag — We've got you covered">
    <!-- base -->
    <rect class="banner__paper" x="0" y="0" width="850" height="256"/>

    <!-- diagonal divider stripe and dark service panel -->
    <polygon class="banner__ink" points="233,0 248,0 343,256 324,256"/>
    <polygon class="banner__ink" points="258,0 850,0 850,256 349,256"/>

    <!-- brand block -->
    <g class="brand">
      <rect class="brand-mark" x="20" y="60" width="34" height="34"/>
      <text class="brand-name" x="20" y="134">CRESTWELL</text>
      <text class="brand-name" x="20" y="166">PRINTS CO</text>
    </g>

    <!-- service checklist -->
    <g class="checklist">
      <polygon class="checkbox" points="300,30 354,30 368,65 314,65"/>
      <polygon class="checkbox" points="358,30 363,30 377,65 372,65"/>

      <polygon class="checkbox" points="324,100 378,100 392,135 338,135"/>
      <polygon class="checkbox" points="382,100 387,100 401,135 396,135"/>

      <polygon class="checkbox" points="348,169 402,169 416,204 362,204"/>
      <polygon class="checkbox" points="406,169 411,169 425,204 420,204"/>
    </g>

    <text class="service" x="392" y="68">SIGNS</text>
    <text class="service" x="419" y="136">SHIRTS</text>
    <text class="service" x="449" y="204">SWAG</text>

    <!-- tagline -->
    <polygon class="tagline-strip" points="371,230 850,230 850,248 378,248"/>
    <text class="tagline" x="389" y="245">WE'VE GOT YOU COVERED</text>
  </svg>
</main>
</body>
</html>
```